Professional and creatice Life Coach - Business Card design

I just relaunched my website and now i a need a correspoonding business card for my task as life coach. My website is www.tbalrond.com as reference. The compass is kind of a symbol for my work, as I help people navigate through their challenging phases in life. The business card should be colorful, but not too playful as I also adress business people. So it sould be creative, but professional (also to suport my other business as Management Consultant)

Target Market(s)

People who want to get teir problems resolved, in business, partnership and other personal realms

Industry/Entity Type

Life Coaching

Contact Information for Business Card

Front side should include Name, Phone number, Email, Website and address

Font styles to use
Sans Serif

Colors
add136

Requirements
Must have
• "Mag. Leopold Brantner" -> Name
"Energetische Praxis" -> Jobtitle (describing my profession as life coach)
colours and style should match my website www.tbalrond.com
Nice to have
• a compass as a symbol

```html
<!DOCTYPE html>
<html lang="de">
<head>
<meta charset="utf-8">
<title>Leopold Brantner – Visitenkarte</title>
<link href="https://fonts.googleapis.com/css2?family=Raleway:wght@500;600;800&display=swap" rel="stylesheet">
<style>
  :root {
    --lime: #add136;
    --ink: #231f20;
    --paper: #fbfbfa;
    --stage: #3a3c3f;
  }
  * { box-sizing: border-box; margin: 0; padding: 0; }
  html, body { width: 1200px; height: 1000px; overflow: hidden; }
  body {
    background: var(--stage);
    font-family: "Raleway", sans-serif;
    position: relative;
  }
  .card {
    position: absolute;
    left: 320px;
    width: 560px;
    height: 320px;
    border-radius: 28px;
    overflow: hidden;
  }
  .card--back {
    top: 110px;
    background: var(--lime);
    display: flex;
    align-items: center;
    justify-content: center;
  }
  .card--front {
    top: 560px;
    background: var(--paper);
  }
  .brand-mark {
    display: flex;
    align-items: center;
    gap: 14px;
    font-weight: 800;
    font-size: 34px;
    letter-spacing: 1px;
    color: var(--ink);
  }
  .brand-mark__dot {
    width: 22px; height: 22px;
    border-radius: 50%;
    background: var(--ink);
  }
  .card--front .brand-mark {
    position: absolute;
    left: 34px;
    top: 142px;
    font-size: 28px;
  }
  .card--front .brand-mark__dot { background: var(--lime); }
  .contact {
    position: absolute;
    right: 30px;
    top: 34px;
    text-align: right;
    color: var(--ink);
  }
  .contact__name {
    font-weight: 800;
    font-size: 23px;
    letter-spacing: 0.3px;
  }
  .contact__title {
    font-weight: 600;
    font-size: 17px;
    color: var(--lime);
    margin-top: 2px;
    margin-bottom: 30px;
  }
  .contact__row {
    display: flex;
    justify-content: flex-end;
    align-items: center;
    gap: 10px;
    font-weight: 500;
    font-size: 16px;
    height: 30px;
  }
  .contact__row--address { margin-top: 40px; }
  .accent { color: var(--lime); }
  .icon { width: 18px; height: 18px; flex: none; }
</style>
</head>
<body>

<section class="card card--back">
  <div class="brand-mark"><span class="brand-mark__dot"></span>Brantner</div>
</section>

<section class="card card--front">
  <div class="brand-mark"><span class="brand-mark__dot"></span>Brantner</div>

  <div class="contact">
    <div class="contact__name">LEOPOLD BRANTNER</div>
    <div class="contact__title">Energetische Praxis</div>

    <div class="contact__row">43 660 4817352
      <svg class="icon" viewBox="0 0 18 18"><rect x="4" y="1" width="10" height="16" rx="2" fill="none" stroke="var(--lime)" stroke-width="2"/><circle cx="9" cy="14" r="1" fill="var(--lime)"/></svg>
    </div>
    <div class="contact__row">leopold<span class="accent">@brantner</span>.one
      <svg class="icon" viewBox="0 0 18 18"><rect x="1" y="4" width="16" height="11" fill="var(--lime)"/><path d="M1 4 L9 10 L17 4" fill="none" stroke="var(--paper)" stroke-width="1.5"/></svg>
    </div>
    <div class="contact__row">www.<span class="accent">tbalrond</span>.com
      <svg class="icon" viewBox="0 0 18 18"><g fill="none" stroke="var(--lime)" stroke-width="1.5"><circle cx="9" cy="9" r="7.5"/><ellipse cx="9" cy="9" rx="3.5" ry="7.5"/><path d="M1.5 9 H16.5 M3 5 H15 M3 13 H15"/></g></svg>
    </div>
    <div class="contact__row contact__row--address">Lindenweg 12, 5020 Salzburg, Austria
      <svg class="icon" viewBox="0 0 18 18"><path d="M9 1 C5 1 3 4 3 7 C3 11 9 17 9 17 C9 17 15 11 15 7 C15 4 13 1 9 1 Z" fill="var(--lime)"/><circle cx="9" cy="7" r="2.3" fill="var(--paper)"/></svg>
    </div>
  </div>
</section>

</body>
</html>
```